I need a business card for my original fine art pieces

I would like a business card design including a logo design for a new business in the art world. I am based in the Hunter Valley NSW Australia. I am a contemporary figurative, encaustic and wildlife artist. I would like to be able to upload my email and mobile number to this as well. This design should be one that I can incorporate into banners and flyers etc. Id like to incorporate one of my own images or partial image into the background or somewhere below. My initials are KD and I would like these used as a logo type. I would like the use of some colour and it to be bright and catchy. The final design should communicate artwork custom made and commissions available.

Overview: Original Fine Artworks for sale, online, art galleries etc, Custom made to order and by commission.

Target market is world wide audience and corporate world

My figurative work is painted using acrylics in a lot of natural ochre colours that reflect the Australian Outback, on canvas, linen, paper or board: My encaustic work is created in a contemporary abstract style using a blow torch and a made with a medium of 100% pure bees wax, Damar resin, mixed media and coloured pigments, applied to Birch board. My wildlife are created using coloured pencil and mixed media on a variety of paper types or board.

```html
<!DOCTYPE html>
<html lang="en">
<head>
<meta charset="utf-8">
<title>Kira Dalton — Business Card</title>
<link href="https://fonts.googleapis.com/css2?family=Open+Sans:wght@400;600;700&display=swap" rel="stylesheet">
<style>
  :root{
    --stage:#1b1b1b;
    --card-dark:#262626;
    --card-dark-2:#161616;
    --paper:#ffffff;
    --accent:#e8501f;
    --ink:#2b2b2b;
    --muted:#555555;
    --light-text:#f2f2f2;
    --ochre-1:#b5651d;
    --ochre-2:#d9a441;
    --ochre-3:#7a3b1a;
  }
  *{box-sizing:border-box;margin:0;padding:0}
  html,body{width:1200px;height:900px;overflow:hidden;background:var(--stage)}
  body{font-family:"Open Sans",sans-serif}
  .stage{position:relative;width:1200px;height:900px}
  .card{position:absolute;width:580px;height:330px;border-radius:30px;overflow:hidden;box-shadow:0 18px 40px rgba(0,0,0,.55)}
  .card--front{left:110px;top:90px;background:linear-gradient(135deg,var(--card-dark) 0%,var(--card-dark-2) 100%)}
  .card--back{left:510px;top:480px;background:var(--paper)}

  .brand{display:flex;align-items:center;gap:14px}
  .brand-dot{width:34px;height:34px;border-radius:50%;background:var(--accent);flex:none}
  .brand-name{font-weight:600;color:var(--accent);font-size:36px;letter-spacing:1px;line-height:1;white-space:nowrap}
  .brand-tagline{font-weight:600;color:var(--light-text);font-size:13px;letter-spacing:4px;margin-top:10px;white-space:nowrap}

  .front-body{position:absolute;left:0;top:0;width:100%;height:262px;display:flex;flex-direction:column;align-items:center;justify-content:center}
  .front-web{margin-top:22px;display:flex;align-items:center;gap:8px;font-size:14px;color:var(--light-text)}
  .front-web .hl,.contact .hl{color:var(--accent)}
  .front-offer{margin-top:10px;font-size:12px;letter-spacing:2px;color:var(--light-text);opacity:.85;text-transform:uppercase}
  .artwork-strip{position:absolute;left:0;bottom:0;width:100%;height:68px;background:linear-gradient(100deg,var(--ochre-3) 0%,var(--ochre-1) 45%,var(--ochre-2) 100%)}

  .back-top{position:absolute;left:0;top:0;width:100%;height:160px;background:linear-gradient(135deg,var(--card-dark) 0%,var(--card-dark-2) 100%);display:flex;flex-direction:column;justify-content:center;padding-left:44px}
  .back-top .brand-name{font-size:34px}
  .back-top .brand-dot{width:30px;height:30px}
  .back-top .brand-tagline{font-size:12px;padding-left:44px}

  .person{position:absolute;left:0;top:212px;width:300px;text-align:center}
  .person-name{font-size:32px;font-weight:700;color:var(--ink);line-height:1}
  .person-name .surname{color:var(--accent);font-weight:600}
  .person-role{font-size:16px;font-weight:600;color:var(--ink);margin-top:6px}
  .divider{position:absolute;left:300px;top:185px;width:1px;height:120px;background:var(--muted)}
  .contact{position:absolute;left:322px;top:180px;font-size:14px;color:var(--ink);line-height:1.45}
  .contact-address{margin-bottom:6px}
  .contact-row{display:flex;align-items:center;gap:9px}
  .icon{width:12px;height:12px;flex:none}
</style>
</head>
<body>
<main class="stage">
  <section class="card card--front">
    <div class="front-body">
      <div class="brand">
        <span class="brand-dot"></span>
        <span class="brand-name">Kira Dalton</span>
      </div>
      <div class="brand-tagline">ORIGINAL FINE ARTWORKS</div>
      <div class="front-web">
        <svg class="icon" viewBox="0 0 12 12" aria-hidden="true"><circle cx="6" cy="6" r="5.2" fill="none" stroke="#e8501f" stroke-width="1.2"/><ellipse cx="6" cy="6" rx="2.3" ry="5.2" fill="none" stroke="#e8501f" stroke-width="1"/><line x1="0.8" y1="6" x2="11.2" y2="6" stroke="#e8501f" stroke-width="1"/></svg>
        <span>www.<span class="hl">kiradaltonart</span>.com</span>
      </div>
      <div class="front-offer">Custom made · Commissions available</div>
    </div>
    <div class="artwork-strip" role="img" aria-label="Strip for a detail of the artist's ochre outback painting"></div>
  </section>

  <section class="card card--back">
    <div class="back-top">
      <div class="brand">
        <span class="brand-dot"></span>
        <span class="brand-name">Kira Dalton</span>
      </div>
      <div class="brand-tagline">ORIGINAL FINE ARTWORKS</div>
    </div>
    <div class="person">
      <div class="person-name">Daniel <span class="surname">Reyes</span></div>
      <div class="person-role">Director</div>
    </div>
    <div class="divider"></div>
    <div class="contact">
      <div class="contact-address">12 Vineyard Lane<br>Sample Town, 1234</div>
      <div class="contact-row">
        <svg class="icon" viewBox="0 0 12 12" aria-hidden="true"><path d="M2.5 1 L4.5 1 L5.2 3.6 L4 4.6 C4.6 6 5.8 7.3 7.3 8 L8.3 6.8 L11 7.4 L11 9.5 C11 10.4 10.3 11 9.4 11 C5 10.6 1.3 7 1 2.6 C1 1.7 1.6 1 2.5 1 Z" fill="#e8501f"/></svg>
        <span>+000 55501 2345</span>
      </div>
      <div class="contact-row">
        <svg class="icon" viewBox="0 0 12 12" aria-hidden="true"><rect x="0.5" y="2" width="11" height="8" rx="1" fill="#e8501f"/><path d="M0.8 2.5 L6 6.6 L11.2 2.5" fill="none" stroke="#fff" stroke-width="1"/></svg>
        <span>hello@kiradalton.com</span>
      </div>
      <div class="contact-row">
        <svg class="icon" viewBox="0 0 12 12" aria-hidden="true"><circle cx="6" cy="6" r="5.5" fill="#e8501f"/><ellipse cx="6" cy="6" rx="2.2" ry="5.5" fill="none" stroke="#fff" stroke-width=".8"/><line x1="0.5" y1="6" x2="11.5" y2="6" stroke="#fff" stroke-width=".8"/></svg>
        <span>www.<span class="hl">kiradaltonart</span>.com</span>
      </div>
    </div>
  </section>
</main>
</body>
</html>
```